Tervolan Pty Ltd professional business card

A professional business card template using the colours from the supplied logo.
Clean crisp lines while, Modern while not being over the top.

Target Market(s)

Construction, commerical and industrial

Industry/Entity Type

Communications

Contact Information for Business Card

For a Communications, IT, Optical fibre installation company

Colors
37b8a4

```html
<!DOCTYPE html>
<html lang="en">
<head>
<meta charset="utf-8">
<title>Tervolan Pty Ltd – Business Card</title>
<link rel="stylesheet" href="https://fonts.googleapis.com/css2?family=Montserrat:wght@400;500;700&display=swap">
<style>
  :root {
    --teal: #1d8e9b;
    --teal-dark: #147382;
    --teal-light: #36a9b5;
    --grey: #5f6064;
    --grey-text: #4a4b4e;
    --paper: #f3f3f3;
    --backdrop: #3b3c3e;
  }
  * { box-sizing: border-box; margin: 0; padding: 0; }
  html, body {
    width: 1200px; height: 900px; overflow: hidden;
    background: var(--backdrop);
    font-family: "Montserrat", sans-serif;
  }
  .stage {
    width: 1200px; height: 900px;
    display: flex; flex-direction: column;
    align-items: center; justify-content: center; gap: 60px;
  }
  .card {
    position: relative;
    width: 560px; height: 320px;
    border-radius: 16px;
    overflow: hidden;
    box-shadow: 0 12px 30px rgba(0,0,0,.45);
  }
  /* back side */
  .card-back {
    background: linear-gradient(135deg, var(--teal) 0%, var(--teal-light) 55%, var(--teal) 100%);
    display: flex; align-items: center; justify-content: center;
  }
  .card-back .brand-name {
    font-weight: 500; font-size: 50px; letter-spacing: 3px;
    color: var(--teal-dark);
  }
  /* front side */
  .card-front { background: var(--paper); }
  .card-front .brand-name {
    position: absolute; left: 44px; top: 44px;
    font-weight: 500; font-size: 40px; letter-spacing: 2px;
    color: var(--grey);
  }
  .holder {
    position: absolute; right: 40px; top: 118px; text-align: right;
  }
  .holder-name {
    font-weight: 700; font-size: 22px; letter-spacing: 2px;
    color: var(--teal); text-transform: uppercase;
  }
  .holder-role {
    font-size: 17px; color: var(--grey-text); letter-spacing: 1px; margin-top: 2px;
  }
  .divider {
    position: absolute; left: 34px; right: 40px; top: 180px;
    height: 2px; background: var(--teal);
  }
  .contact-list {
    position: absolute; left: 34px; top: 192px; list-style: none;
    font-size: 13.5px; color: var(--grey-text); letter-spacing: .5px; line-height: 20px;
  }
  .contact-list li { display: flex; align-items: center; gap: 8px; }
  .contact-list svg { width: 13px; height: 13px; fill: var(--teal); flex: none; }
  .address {
    position: absolute; right: 40px; top: 196px; text-align: right;
    font-size: 13.5px; color: var(--grey-text); letter-spacing: .8px; line-height: 20px;
  }
  .footer-band {
    position: absolute; left: 0; bottom: 0; width: 560px; height: 80px;
  }
  .website {
    position: absolute; right: 36px; bottom: 12px;
    font-size: 14px; color: #fff; letter-spacing: 1px;
  }
</style>
</head>
<body>
<main class="stage">
  <section class="card card-back">
    <span class="brand-name">TERVOLAN</span>
  </section>

  <section class="card card-front">
    <span class="brand-name">TERVOLAN</span>

    <div class="holder">
      <p class="holder-name">Darren Kowalski</p>
      <p class="holder-role">Director</p>
    </div>

    <div class="divider"></div>

    <ul class="contact-list">
      <li>
        <svg viewBox="0 0 24 24"><path d="M6.6 10.8a15 15 0 0 0 6.6 6.6l2.2-2.2c.3-.3.7-.4 1-.2 1.1.4 2.3.6 3.6.6.6 0 1 .4 1 1V20c0 .6-.4 1-1 1A17 17 0 0 1 3 4c0-.6.4-1 1-1h3.5c.6 0 1 .4 1 1 0 1.3.2 2.5.6 3.6.1.3 0 .7-.2 1z"/></svg>
        947 318 2206
      </li>
      <li>
        <svg viewBox="0 0 24 24"><path d="M7 1h10a2 2 0 0 1 2 2v18a2 2 0 0 1-2 2H7a2 2 0 0 1-2-2V3a2 2 0 0 1 2-2zm0 3v14h10V4zm5 15.5a1 1 0 1 0 0 2 1 1 0 0 0 0-2z"/></svg>
        215 603 4478
      </li>
      <li>
        <svg viewBox="0 0 24 24"><path d="M2 5h20v2l-10 6L2 7zm0 4.3 10 6 10-6V19H2z"/></svg>
        info@tervolan.com
      </li>
    </ul>

    <p class="address">Level 2, 17 Harwick Lane<br>Brenton, VIC 3152</p>

    <svg class="footer-band" viewBox="0 0 560 80" preserveAspectRatio="none">
      <path d="M0 26 C 160 6, 320 8, 480 38" fill="none" stroke="var(--grey)" stroke-width="5"/>
      <path d="M40 30 C 220 16, 420 22, 560 56 L560 80 L0 80 L0 34 Z" fill="var(--teal-dark)"/>
    </svg>
    <span class="website">www.tervolan.com</span>
  </section>
</main>
</body>
</html>
```